crumbs of morning project

I need 2 stickers (lid and side) for a see-through rectangular plastic container that holds a whole, free range chicken.
Updates

CHANGE OF PACKAGING

 

we are unable to source the clear, rectangular, see-throughcontainer in the previously attached file and have to amend our packagingstrategy.

 

 

 

UPDATED STRATEGY:

 

we intend to use one of the 'french style' cardboard typewrap-around stickers as shown in the new attachments I have posted. australiansupermarkets would not accept this type of thin cardboard on its own as is applicablein france and for that reason we intend insert the wrapped-around cardboard stickeredwhole chicken on a poly styrene tray and then placed in a clear plastic cellophanebag with a twisted tie as shown the 'varnot brand' attached file.

 

the other technical requirements (barcode, kilograms, netpricing, etc.) remain the same

 

 

also note:

 

when using our existing 'seal pure' logo, please removethe text:

 

rabbi tovah lindquist haber

potential brand names:

1. crumbs of morning
2. brisk olando

cardboard label needs to be a ' wrap around label' (wrapped, north-south) as shown in the following 
attached files:

'wrap around label'  + 'wrap around label b'

we like the 'brisk olando' FONT and primary yellow background. 

dorvid 

Target Market(s)

free range poultry consumers (GREENIES) jews (seal pure), affluent, up market, product is priced at the premium end of the market

Industry/Entity Type

Plastic

Requirements
Must have
• in order of importance...

LID LABEL STICKER-(see attached photo)
logo name (crumbs of morning)
free range
sanitised with kosher rock salt
extra fresh
long shelf life
kosher certified

SIDE LABEL STICKER- (see attached photo)
country of manufacture
processors contact details
(7 pellbrook lane ashvale west 3290 0487 220 318 www.crumbsofmorning.com.au)
barcode
product description (whole, drumsticks, filets, etc)
kosher status declaration and kosher logo (see attachment)
price per kilogram section
net weight per kilogram section
use by date
total price
refrigeration advise-store below 5degreesC

note:

the whole chicken is wrapped in light BROWN colored butchers paper and tied with a green ribbon. the customer can only see the raw chicken at each end.

```html
<!DOCTYPE html>
<html lang="en">
<head>
<meta charset="utf-8">
<title>Sunny Marlow – Wrap Around Label Options</title>
<link href="https://fonts.googleapis.com/css2?family=Cinzel:wght@500;700&family=Tinos:wght@400;700&family=Raleway:wght@500&display=swap" rel="stylesheet">
<style>
  :root{
    --stage-light:#d6d6d6;
    --stage-mid:#9c9c9c;
    --band-center:#3d3d3d;
    --band-edge:#050505;
    --label-top:#f9ab12;
    --label-bottom:#f28a2a;
    --outline:#7a4a05;
    --panel:#0b0b0b;
    --panel-rim:#f5b21a;
    --feature-black:#0d0d0d;
    --feature-red:#8c1a16;
    --seal-red:#9a1b16;
    --gold:#f4b216;
    --name-gold:#6e4402;
    --name-bronze:#7f5206;
    --ink:#151515;
    --web-ink:#5a3300;
    --note:#8e8e8e;
    --white:#ffffff;
    --origin:#7a1010;
  }
  html,body{margin:0;padding:0;overflow:hidden;}
  body{width:1200px;height:900px;background:linear-gradient(180deg,var(--stage-mid) 0%,var(--stage-light) 50%,var(--stage-mid) 100%);}
  svg.board{display:block;width:1200px;height:900px;}
  .option-number{font:500 17px "Raleway",sans-serif;fill:var(--note);}
  .note{font:500 14px "Raleway",sans-serif;fill:var(--note);text-anchor:middle;letter-spacing:.5px;}
  .note-large{font-size:19px;}
  .note-line{stroke:var(--note);stroke-width:1.6;fill:none;}
  .feature{font-family:"Cinzel",serif;font-weight:700;fill:var(--white);text-anchor:middle;}
  .feature.large{font-size:12.5px;}
  .feature.small{font-size:11px;}
  .brand-name{font-family:"Cinzel",serif;font-weight:700;text-anchor:middle;font-size:31px;}
  .tagline{font-family:"Tinos",serif;font-weight:700;fill:var(--ink);text-anchor:middle;}
  .cuts{font-family:"Cinzel",serif;font-weight:500;fill:var(--gold);text-anchor:middle;}
  .field{font-family:"Tinos",serif;font-weight:700;fill:var(--ink);}
  .origin{font-family:"Tinos",serif;font-weight:700;fill:var(--origin);text-anchor:middle;font-size:11px;}
  .address{font-family:"Tinos",serif;fill:var(--white);text-anchor:middle;font-size:10px;}
  .web{font-family:"Cinzel",serif;font-weight:700;fill:var(--web-ink);text-anchor:middle;font-size:11px;}
</style>
</head>
<body>
<svg class="board" viewBox="0 0 1200 900" xmlns="http://www.w3.org/2000/svg">
  <defs>
    <radialGradient id="band-glow" cx="50%" cy="45%" r="60%">
      <stop offset="0" stop-color="var(--band-center)"/>
      <stop offset="1" stop-color="var(--band-edge)"/>
    </radialGradient>
    <linearGradient id="label-fill" x1="0" y1="0" x2="0" y2="1">
      <stop offset="0" stop-color="var(--label-top)"/>
      <stop offset="1" stop-color="var(--label-bottom)"/>
    </linearGradient>
    <symbol id="label-body" viewBox="0 0 306 760" overflow="visible">
      <path d="M78,128 Q153,121 228,128 Q240,131 238,150 Q232,182 210,200 L210,410 Q212,470 280,540 Q298,565 298,600 L298,715 Q298,740 270,743 Q153,753 36,743 Q8,740 8,715 L8,600 Q8,565 26,540 Q94,470 96,410 L96,200 Q74,182 68,150 Q66,131 78,128 Z" fill="url(#label-fill)" stroke="var(--outline)" stroke-width="1.5"/>
      <path d="M102,196 L204,196 L204,412 Q204,428 190,428 L116,428 Q102,428 102,412 Z" fill="var(--panel)" stroke="var(--panel-rim)" stroke-width="2"/>
      <g fill="var(--box)" stroke="var(--panel-rim)" stroke-width="2">
        <rect x="105" y="207" width="96" height="43" rx="7"/>
        <rect x="105" y="262" width="96" height="43" rx="7"/>
        <rect x="105" y="317" width="96" height="43" rx="7"/>
        <rect x="105" y="372" width="96" height="43" rx="7"/>
      </g>
      <rect class="seal-badge" x="128" y="512" width="84" height="22" rx="2" fill="var(--seal-red)"/>
      <rect x="30" y="579" width="246" height="24" fill="var(--band)"/>
      <rect x="14" y="610" width="194" height="95" fill="var(--white)"/>
    </symbol>
  </defs>

  <rect class="display-band" x="0" y="110" width="1200" height="650" fill="url(#band-glow)"/>

  <text class="option-number" x="36" y="160">1</text>
  <text class="option-number" x="338" y="160">2</text>
  <text class="option-number" x="640" y="160">3</text>
  <text class="option-number" x="940" y="160">4</text>

  <!-- Option 1 -->
  <g class="label-option" transform="translate(2 0)">
    <use href="#label-body" x="0" y="0" width="306" height="760" style="--box:var(--feature-black);--band:var(--panel)"/>
    <text class="feature large" x="153" y="222">Breed of<tspan x="153" dy="12">Poultry:</tspan><tspan x="153" dy="12">Corra</tspan></text>
    <text class="feature large" x="153" y="281">Purified<tspan x="153" dy="12">with Salt</tspan></text>
    <text class="feature large" x="153" y="336">Extended<tspan x="153" dy="12">Shelf Life</tspan></text>
    <text class="feature large" x="153" y="391">Kosher<tspan x="153" dy="12">Certified</tspan></text>
    <text class="brand-name" x="153" y="468" fill="var(--ink)">Sunny<tspan x="153" dy="33">Marlow</tspan></text>
    <text class="tagline" x="153" y="556" font-size="13.5">Extra Fresh, Long Shelf Life</text>
    <text class="tagline" x="153" y="572" font-size="14.5">Store Below 5°C</text>
    <text class="cuts" x="153" y="596" font-size="14.5">Whole, Drumsticks, Filets, etc.</text>
    <text class="field" x="26" y="629" font-size="12.5">Best Before:</text>
    <text class="field" x="26" y="652" font-size="12.5">Price per kg:</text>
    <text class="field" x="20" y="675" font-size="12.5">Net wt per kg:</text>
    <text class="field" x="30" y="698" font-size="12.5">Total price:</text>
    <text class="origin" x="241" y="676">Product<tspan x="241" dy="10">of</tspan><tspan x="241" dy="10">Australia</tspan></text>
    <text class="address" x="153" y="724">7 Pellbrook Lane, Ashvale West 3290 0487 220 318</text>
    <text class="web" x="153" y="738">www.SunnyMarlow.com.au</text>
  </g>

  <!-- Option 2 -->
  <g class="label-option" transform="translate(304 0)">
    <use href="#label-body" x="0" y="0" width="306" height="760" style="--box:var(--feature-black);--band:var(--panel)"/>
    <text class="feature small" x="153" y="221">Breed of<tspan x="153" dy="12">Poultry:</tspan><tspan x="153" dy="12">Corra</tspan></text>
    <text class="feature small" x="153" y="281">Purified<tspan x="153" dy="12">with Salt</tspan></text>
    <text class="feature small" x="153" y="336">Extended<tspan x="153" dy="12">Shelf Life</tspan></text>
    <text class="feature small" x="153" y="391">Kosher<tspan x="153" dy="12">Certified</tspan></text>
    <text class="brand-name" x="153" y="468" fill="var(--name-gold)">Sunny<tspan x="153" dy="33">Marlow</tspan></text>
    <text class="tagline" x="153" y="556" font-size="13">Extra Fresh, Long Shelf Life</text>
    <text class="tagline" x="153" y="572" font-size="13.5">Store Below 5°C</text>
    <text class="cuts" x="153" y="596" font-size="13">Whole, Drumsticks, Filets, etc.</text>
    <text class="field" x="28" y="629" font-size="11.5">Best Before:</text>
    <text class="field" x="28" y="652" font-size="11.5">Price per kg:</text>
    <text class="field" x="22" y="675" font-size="11.5">Net wt per kg:</text>
    <text class="field" x="32" y="698" font-size="11.5">Total price:</text>
    <text class="origin" x="241" y="676">Product<tspan x="241" dy="10">of</tspan><tspan x="241" dy="10">Australia</tspan></text>
    <text class="address" x="153" y="724">7 Pellbrook Lane, Ashvale West 3290 0487 220 318</text>
    <text class="web" x="153" y="738">www.SunnyMarlow.com.au</text>
  </g>

  <!-- Option 3 -->
  <g class="label-option" transform="translate(606 0)">
    <use href="#label-body" x="0" y="0" width="306" height="760" style="--box:var(--feature-black);--band:var(--panel)"/>
    <text class="feature small" x="153" y="221">Breed of<tspan x="153" dy="12">Poultry:</tspan><tspan x="153" dy="12">Corra</tspan></text>
    <text class="feature small" x="153" y="281">Purified<tspan x="153" dy="12">with Salt</tspan></text>
    <text class="feature small" x="153" y="336">Extended<tspan x="153" dy="12">Shelf Life</tspan></text>
    <text class="feature small" x="153" y="391">Kosher<tspan x="153" dy="12">Certified</tspan></text>
    <text class="brand-name" x="153" y="468" fill="var(--name-bronze)">Sunny<tspan x="153" dy="33">Marlow</tspan></text>
    <text class="tagline" x="153" y="556" font-size="12.5">Extra Fresh, Long Shelf Life</text>
    <text class="tagline" x="153" y="571" font-size="13">Store Below 5°C</text>
    <text class="cuts" x="153" y="595" font-size="12.5">Whole, Drumsticks, Filets, etc.</text>
    <text class="field" x="26" y="630" font-size="11">Best Before:</text>
    <text class="field" x="26" y="652" font-size="11">Price per kg:</text>
    <text class="field" x="20" y="674" font-size="11">Net wt per kg:</text>
    <text class="field" x="30" y="696" font-size="11">Total price:</text>
    <text class="origin" x="241" y="676">Product<tspan x="241" dy="10">of</tspan><tspan x="241" dy="10">Australia</tspan></text>
    <text class="address" x="153" y="724">7 Pellbrook Lane, Ashvale West 3290 0487 220 318</text>
    <text class="web" x="153" y="738">www.SunnyMarlow.com.au</text>
  </g>

  <!-- Option 4 -->
  <g class="label-option" transform="translate(896 0)">
    <use href="#label-body" x="0" y="0" width="306" height="760" style="--box:var(--feature-red);--band:var(--feature-red)"/>
    <text class="feature small" x="153" y="221">Breed of<tspan x="153" dy="12">Poultry:</tspan><tspan x="153" dy="12">Corra</tspan></text>
    <text class="feature small" x="153" y="281">Purified<tspan x="153" dy="12">with Salt</tspan></text>
    <text class="feature small" x="153" y="336">Extended<tspan x="153" dy="12">Shelf Life</tspan></text>
    <text class="feature small" x="153" y="391">Kosher<tspan x="153" dy="12">Certified</tspan></text>
    <text class="brand-name" x="153" y="468" fill="var(--name-bronze)">Sunny<tspan x="153" dy="33">Marlow</tspan></text>
    <text class="tagline" x="153" y="556" font-size="12.5">Extra Fresh, Long Shelf Life</text>
    <text class="tagline" x="153" y="571" font-size="13">Store Below 5°C</text>
    <text class="cuts" x="153" y="595" font-size="12.5" fill="var(--white)">Whole, Drumsticks, Filets, etc.</text>
    <text class="field" x="26" y="630" font-size="11">Best Before:</text>
    <text class="field" x="26" y="652" font-size="11">Price per kg:</text>
    <text class="field" x="20" y="674" font-size="11">Net wt per kg:</text>
    <text class="field" x="30" y="696" font-size="11">Total price:</text>
    <text class="origin" x="241" y="676">Product<tspan x="241" dy="10">of</tspan><tspan x="241" dy="10">Australia</tspan></text>
    <text class="address" x="153" y="724">7 Pellbrook Lane, Ashvale West 3290 0487 220 318</text>
    <text class="web" x="153" y="738">www.SunnyMarlow.com.au</text>
  </g>

  <!-- Design notes -->
  <g class="design-notes">
    <text class="note" x="599" y="268">Proportionately</text>
    <text class="note" x="599" y="286">Smaller</text>
    <text class="note" x="599" y="304">Text for Features &amp;</text>
    <text class="note" x="599" y="322">Other Text</text>
    <line class="note-line" x1="522" y1="263" x2="538" y2="263"/>
    <line class="note-line" x1="662" y1="263" x2="678" y2="263"/>
    <line class="note-line" x1="522" y1="300" x2="530" y2="300"/>
    <line class="note-line" x1="668" y1="300" x2="676" y2="300"/>

    <text class="note note-large" x="593" y="380">Gold Text</text>
    <text class="note note-large" x="593" y="406">Variations</text>
    <polyline class="note-line" points="545,463 591,420 641,463"/>

    <text class="note note-large" x="880" y="282">Color</text>
    <text class="note note-large" x="880" y="308">from “Seal</text>
    <text class="note note-large" x="880" y="334">Pure”</text>
    <text class="note note-large" x="880" y="360">Added</text>
    <line class="note-line" x1="934" y1="287" x2="952" y2="287"/>
    <circle cx="938" cy="346" r="1.3" fill="var(--note)"/>
    <circle cx="947" cy="346" r="1.3" fill="var(--note)"/>
    <path class="note-line" d="M935,351 Q942,358 950,351"/>
  </g>
</svg>
</body>
</html>
```